We are a music event management company based out of Syracuse, NY but we do business in multiple areas like the mid-west and Florida.

Our primary events revolve around the Electronic Dance Music scene. (acts like Brinmoor, Nordic Loft Syndicate, Dorian Pell)

We would like a clean cut business card with Voltaramble written on the back. In Voltaramble we would like the u to be shaped like a sixteenth note. The colors green and silver would be nice to see somehow but not necessary. Feel free to play around with it and have fun because that's what our business is about, Having Fun!

Some similar examples for reference would be the Neon Orchard or Glowing Tulip Jamboree website.

Our goal is to provide people with an experience, not just a concert. There is a difference.

Reason: Needed more time to decide.

Industry/Entity Type

Events

```html
<!DOCTYPE html>
<html lang="en">
<head>
<meta charset="utf-8">
<title>Voltaramble Business Card</title>
<link href="https://fonts.googleapis.com/css2?family=Arimo:wght@400;700&display=swap" rel="stylesheet">
<style>
  :root {
    --page-bg: #e9e6e3;
    --front-core: #1a4fb0;
    --front-mid: #0b2a66;
    --front-edge: #03102a;
    --back-bg: #050505;
    --silver: #c7cad0;
    --white: #ffffff;
    --accent-blue: #4aa3ec;
    --tab-blue: #0f4fa8;
    --note-light: #3fa0f0;
    --note-deep: #0a3a8c;
  }
  html, body {
    margin: 0;
    padding: 0;
    width: 1200px;
    height: 1000px;
    overflow: hidden;
    background: var(--page-bg);
    font-family: "Arimo", Arial, sans-serif;
  }
  .canvas {
    position: relative;
    width: 1200px;
    height: 1000px;
  }
  .card {
    position: absolute;
    left: 267px;
    width: 652px;
    height: 372px;
    border-radius: 18px;
    overflow: hidden;
  }
  .card-front {
    top: 91px;
    background: radial-gradient(ellipse 340px 220px at 50% 52%, var(--front-core) 0%, var(--front-mid) 55%, var(--front-edge) 100%);
  }
  .card-back {
    top: 529px;
    background: var(--back-bg);
  }
  .note-border {
    position: absolute;
    top: 0;
    height: 100%;
  }
  .note-border--left {
    left: 0;
    width: 78px;
    background: linear-gradient(90deg, var(--note-light) 0%, var(--note-deep) 55%, rgba(10,58,140,0) 100%);
    opacity: 0.85;
  }
  .note-border--right {
    right: 0;
    width: 96px;
    background: linear-gradient(270deg, var(--note-light) 0%, var(--note-deep) 60%, rgba(10,58,140,0) 100%);
    opacity: 0.9;
  }
  .wordmark {
    position: absolute;
    left: 50px;
    width: 652px;
    text-align: center;
    color: var(--silver);
    font-weight: 400;
    font-size: 50px;
    letter-spacing: 7px;
    line-height: 1;
  }
  .card-front .wordmark { top: 164px; left: 0; }
  .tagline {
    position: absolute;
    top: 220px;
    left: 0;
    width: 100%;
    text-align: center;
    color: var(--white);
    font-size: 17px;
    letter-spacing: 6px;
    font-weight: 400;
  }
  .card-back .wordmark { top: 47px; left: 0; }
  .holder-name {
    position: absolute;
    top: 108px;
    left: 0;
    width: 100%;
    text-align: center;
    color: var(--white);
    font-weight: 700;
    font-size: 23px;
  }
  .holder-role { color: var(--accent-blue); }
  .mailing-address {
    position: absolute;
    top: 156px;
    right: 174px;
    text-align: right;
    color: var(--white);
    font-weight: 700;
    font-size: 18px;
    line-height: 27px;
  }
  .icon-tab {
    position: absolute;
    left: 0;
    top: 213px;
    width: 49px;
    height: 104px;
    background: var(--tab-blue);
    border-radius: 0 4px 4px 0;
  }
  .icon-tab svg {
    position: absolute;
    left: 15px;
    width: 20px;
    height: 20px;
  }
  .contact-list {
    position: absolute;
    left: 76px;
    top: 222px;
    margin: 0;
    padding: 0;
    list-style: none;
    color: var(--white);
    font-weight: 700;
    font-size: 16px;
  }
  .contact-list li { height: 32px; }
</style>
</head>
<body>
<main class="canvas">

  <section class="card card-front">
    <div class="note-border note-border--left" role="img" aria-label="Scattered blue music notes decoration along the left edge"></div>
    <div class="note-border note-border--right" role="img" aria-label="Scattered blue music notes decoration along the right edge"></div>
    <div class="wordmark">Voltaramble</div>
    <div class="tagline">MORE THAN A SHOW</div>
  </section>

  <section class="card card-back">
    <div class="note-border note-border--right" role="img" aria-label="Scattered blue music notes decoration along the right edge"></div>
    <div class="wordmark">Voltaramble</div>
    <div class="holder-name">Marcus T Delvane <span class="holder-role">CEO</span></div>
    <div class="mailing-address">PO 418<br>Halvern PA 16420</div>

    <div class="icon-tab">
      <svg style="top:8px" viewBox="0 0 24 24" fill="none" stroke="#fff" stroke-width="1.5" aria-hidden="true">
        <path d="M5 3h4l2 5-2.5 1.5a11 11 0 0 0 6 6L16 13l5 2v4a2 2 0 0 1-2 2A17 17 0 0 1 3 5a2 2 0 0 1 2-2z"/>
      </svg>
      <svg style="top:41px" viewBox="0 0 24 24" fill="none" stroke="#fff" stroke-width="1.5" aria-hidden="true">
        <rect x="3" y="5" width="18" height="14"/>
        <path d="M3 5l9 8 9-8M3 19l7-7M21 19l-7-7"/>
      </svg>
      <svg style="top:74px" viewBox="0 0 24 24" fill="none" stroke="#fff" stroke-width="1.5" aria-hidden="true">
        <circle cx="12" cy="12" r="9"/>
        <ellipse cx="12" cy="12" rx="4" ry="9"/>
        <path d="M3 12h18M4.5 7.5h15M4.5 16.5h15"/>
      </svg>
    </div>

    <ul class="contact-list">
      <li>315-555-0142</li>
      <li>marcus@voltarambleny.com</li>
      <li>www.voltarambleny.com</li>
    </ul>
  </section>

</main>
</body>
</html>
```